Handyman Business Card and website logo design

I need a logo for my new handyman business. The logo will be used for my website, business cards, and Facebook pages. I want my business card to have this logo and have a simplistic and nicely flowing design with a handyman feel.

The name of my business is KT Fixit Pro. (Dr is for doctor NOT Drive). So my thoughts for my logo is a handyman with a stethoscope and looking like a doctor examining a house. With handyman will have a tool-belt on and holding a drill or some other well recognized tool. Basically a handyman doctor examining someones "precious home" so that he can prescribe the right "fix" for them.

Industry/Entity Type

Business

Contact Information for Business Card

Marcus Pellworth (CEO)
KTFixitPro
4719 Winterfold Lane
Brookhaven, OH 60718

```html
<!DOCTYPE html>
<html lang="en">
<head>
<meta charset="utf-8">
<title>KT Fixit Pro – Business Card</title>
<link rel="stylesheet" href="https://fonts.googleapis.com/css2?family=Tinos:wght@400;700&family=Open+Sans:wght@400;600&display=swap">
<style>
  :root {
    --page-bg: #e9e6e1;
    --card-white: #f4f4f4;
    --ink-navy: #0f1b33;
    --ink-dark: #1c1c1c;
    --band-black: #050505;
    --band-gray: #a9a9a9;
    --text-white: #ffffff;
    --photo-light: #f1efee;
    --photo-mid: #c9c4c2;
    --serif: "Tinos", "Times New Roman", serif;
    --sans: "Open Sans", Arial, sans-serif;
  }
  html, body {
    margin: 0;
    width: 1200px;
    height: 892px;
    overflow: hidden;
    background: var(--page-bg);
  }
  .canvas {
    position: relative;
    width: 1200px;
    height: 892px;
  }
  .card {
    position: absolute;
    left: 250px;
    width: 700px;
    height: 400px;
    overflow: hidden;
    background: var(--card-white);
    box-shadow: 0 6px 18px rgba(0,0,0,0.18);
  }
  .card--front { top: 26px; }
  .card--back { top: 466px; }

  /* front */
  .front-swoosh {
    position: absolute;
    inset: 0;
    width: 700px;
    height: 400px;
  }
  .brand-name {
    position: absolute;
    left: 44px;
    top: 36px;
    margin: 0;
    font-family: var(--serif);
    font-weight: 400;
    font-size: 84px;
    line-height: 1;
    color: var(--ink-navy);
    letter-spacing: -1px;
  }
  .person {
    position: absolute;
    left: 70px;
    top: 160px;
    width: 230px;
    text-align: center;
    font-family: var(--serif);
    color: var(--ink-dark);
  }
  .person__name { font-size: 28px; margin: 0; }
  .person__role { font-size: 24px; margin: 0; }
  .divider {
    position: absolute;
    left: 322px;
    top: 140px;
    width: 1px;
    height: 86px;
    background: var(--ink-dark);
  }
  .contacts {
    position: absolute;
    left: 342px;
    top: 140px;
    margin: 0;
    padding: 0;
    list-style: none;
    font-family: var(--sans);
    font-size: 19px;
    color: var(--ink-dark);
  }
  .contacts li {
    display: flex;
    align-items: center;
    gap: 12px;
    height: 29px;
  }
  .contacts svg { width: 14px; height: 14px; flex: none; }
  .address {
    font-family: var(--sans);
    font-size: 20px;
    fill: var(--text-white);
    letter-spacing: 0.3px;
  }

  /* back */
  .photo-area {
    position: absolute;
    inset: 0;
    background:
      radial-gradient(ellipse at 62% 40%, #ffffff 0%, rgba(255,255,255,0) 45%),
      linear-gradient(180deg, var(--photo-mid) 0%, var(--photo-light) 55%, #ffffff 100%);
  }
  .back-name {
    position: absolute;
    left: 0;
    right: 0;
    bottom: 48px;
    margin: 0;
    text-align: center;
    font-family: var(--serif);
    font-weight: 400;
    font-size: 92px;
    line-height: 1;
    color: var(--ink-dark);
  }
</style>
</head>
<body>
<main class="canvas">

  <section class="card card--front" aria-label="Business card front">
    <svg class="front-swoosh" viewBox="0 0 700 400" aria-hidden="true">
      <path d="M40,400 C260,330 500,250 700,130 L700,146 C500,268 270,346 70,400 Z" fill="var(--band-gray)"/>
      <path d="M110,400 C330,345 540,262 700,178 L700,400 Z" fill="var(--band-black)"/>
      <path id="addressLine" d="M230,396 C410,356 580,300 700,240" fill="none"/>
      <text class="address"><textPath href="#addressLine" startOffset="50">4719 Winterfold Lane Brookhaven, OH 60718</textPath></text>
    </svg>

    <h1 class="brand-name">KT Fixit Pro</h1>

    <div class="person">
      <p class="person__name">Marcus Pellworth</p>
      <p class="person__role">CEO</p>
    </div>

    <div class="divider"></div>

    <ul class="contacts">
      <li>
        <svg viewBox="0 0 14 14" aria-hidden="true"><rect width="14" height="14" fill="var(--ink-dark)"/><path d="M4,3 L6,3 L6.5,5.5 L5.5,6.5 C6,8 7,9 8.5,9.5 L9.5,8.5 L12,9 L12,11 C7,11 3,7 3,3 Z" fill="#fff"/></svg>
        <span>94 5120 3348</span>
      </li>
      <li>
        <svg viewBox="0 0 14 14" aria-hidden="true"><rect width="14" height="14" fill="var(--ink-dark)"/><circle cx="7" cy="7" r="4" fill="none" stroke="#fff" stroke-width="1.2"/><line x1="3" y1="7" x2="11" y2="7" stroke="#fff" stroke-width="1"/></svg>
        <span>www.ktfixitpro</span>
      </li>
      <li>
        <svg viewBox="0 0 14 14" aria-hidden="true"><rect width="14" height="14" fill="var(--ink-dark)"/><rect x="3" y="4.5" width="8" height="5.5" fill="#fff"/><path d="M3,4.5 L7,7.5 L11,4.5" fill="none" stroke="var(--ink-dark)" stroke-width="1"/></svg>
        <span>ktfixitpro@email.com</span>
      </li>
    </ul>
  </section>

  <section class="card card--back" aria-label="Business card back">
    <div class="photo-area" role="img" aria-label="Photo of a small white model house with red shutters beside a stethoscope on a soft grey surface"></div>
    <h2 class="back-name">KT Fixit Pro</h2>
  </section>

</main>
</body>
</html>
```